Realty Group Needs Classy, Contemporary Letterhead Design

We need a letterhead design for a new realty company located in NY, USA. We buy investment properties to rehabilitate and or keep in our rental portfolio.

```html
<!DOCTYPE html>
<html lang="en">
<head>
<meta charset="utf-8">
<title>Meridian Realty Group — Letterhead</title>
<link rel="stylesheet" href="https://fonts.googleapis.com/css2?family=Rubik:ital,wght@0,300;0,700;1,300&display=swap">
<style>
  :root {
    --backdrop: #b894de;
    --paper: #f7f6f8;
    --brand: #431592;
    --brand-soft: #5b2db3;
    --ink: #2b2733;
    --wash: #ebe5f3;
    --white: #ffffff;
  }
  * { box-sizing: border-box; margin: 0; padding: 0; }
  html, body { width: 1200px; height: 800px; overflow: hidden; }
  body {
    background: var(--backdrop);
    font-family: "Rubik", Arial, sans-serif;
    position: relative;
  }
  .letterhead {
    position: absolute;
    left: 331px; top: 20px;
    width: 537px; height: 760px;
    background: var(--paper);
    overflow: hidden;
    box-shadow: 0 6px 22px rgba(60, 20, 110, 0.25);
  }
  .company-name {
    position: absolute; left: 0; right: 0; top: 62px;
    display: flex; justify-content: center; align-items: center; gap: 9px;
    font-weight: 700; font-size: 20px; letter-spacing: 0.4px;
    color: var(--brand); white-space: nowrap;
  }
  .company-square {
    width: 12px; height: 12px; background: var(--brand);
  }
  .sender-name {
    position: absolute; left: 59px; top: 170px;
    font-weight: 700; font-size: 22px; line-height: 1; color: var(--brand);
  }
  .sender-role {
    position: absolute; left: 59px; top: 196px;
    font-weight: 300; font-size: 16px; line-height: 1; color: var(--brand-soft);
  }
  .letter-date {
    position: absolute; right: 59px; top: 203px;
    font-weight: 300; font-size: 12px; line-height: 1; color: var(--brand-soft);
  }
  .letter-body {
    position: absolute; left: 54px; top: 243px; width: 429px;
    font-weight: 300; font-size: 11.2px; line-height: 23px;
    color: var(--ink); text-align: justify;
  }
  .signature-mark {
    position: absolute; left: 350px; top: 585px;
    width: 122px; height: 36px;
    background: linear-gradient(90deg, rgba(91,45,179,0.10), rgba(91,45,179,0.03));
    border-radius: 18px;
  }
  .signatory {
    position: absolute; left: 350px; width: 122px; top: 638px;
    text-align: center;
    font-style: italic; font-weight: 300; font-size: 13.5px; line-height: 1;
    color: var(--brand-soft);
  }
  .contact-band {
    position: absolute; left: 154px; right: 0; top: 717px; height: 21px;
    background: var(--brand);
    display: flex; align-items: center; justify-content: space-around;
    padding: 0 8px;
    color: var(--white); font-weight: 300; font-size: 9.5px;
  }
  .contact-item { display: flex; align-items: center; gap: 5px; white-space: nowrap; }
  .contact-item svg { width: 10px; height: 10px; fill: none; stroke: var(--white); stroke-width: 1.4; }
</style>
</head>
<body>
  <main class="letterhead">
    <div class="company-name"><span class="company-square"></span>Meridian Realty Group, LLC</div>

    <div class="sender-name">NAME SURNAME</div>
    <div class="sender-role">MANAGER</div>
    <div class="letter-date">Dec. 28, 2021</div>

    <div class="letter-body">
      <p>Lorem ipsum dolor sit amet, consectetuer adipiscing elit, sed diam nonummy nibh euismod tincidunt ut laoreet dolore magna aliquam erat volutpat. Ut wisi enim ad minim veniam, quis nostrud exerci tation ullamcorper suscipit lobortis nisl ut aliquip ex ea commodo consequat. qui blandit praesent luptatum zzril delenit augue duis dolore te feugait nulla facilisi.</p>
      <p>Lorem ipsum dolor sit amet, cons ectetuer adipiscing elit, sed diam nonummy nibh euismod tincidunt ut laoreet dolore magna aliquam erat volutpat. Ut wisi enim ad minim veniam, quis nostrud exerci tation ullamcorper suscipit lobortis nisl ut aliquip ex ea commodo consequat.</p>
      <p>Lorem ipsum dolor sit amet, consectetuer adipiscing elit, sed diam nonummy nibh euismod tincidunt ut laoreet dolore magna aliquam erat volutpat. Ut wisi enim ad minim veniam,vel illum dolore eu feugiat nulla facilisis at vero eros et accumsan et iusto odio dignissim qui blandit praesent luptatum zzril delenit augue duis dolore te feugait nulla facilisi.</p>
    </div>

    <div class="signature-mark" role="img" aria-label="Handwritten signature"></div>
    <div class="signatory">LOREM IPSUM</div>

    <footer class="contact-band">
      <span class="contact-item">
        <svg viewBox="0 0 12 12" aria-hidden="true"><rect x="1" y="2.5" width="10" height="7" rx="0.8"/><path d="M1.3 3l4.7 3.6L10.7 3"/></svg>
        info@meridianrealty.net
      </span>
      <span class="contact-item">
        <svg viewBox="0 0 12 12" aria-hidden="true"><path d="M2.5 1.5l2 0 .8 2.4-1.3 1c.6 1.3 1.6 2.3 2.9 2.9l1-1.3 2.4.8v2c0 .5-.4.9-.9.9C5 10.2 1.8 7 1.6 2.4c0-.5.4-.9.9-.9z"/></svg>
        +1 212 555 0147
      </span>
      <span class="contact-item">
        <svg viewBox="0 0 12 12" aria-hidden="true"><circle cx="6" cy="6" r="4.8"/><ellipse cx="6" cy="6" rx="2" ry="4.8"/><path d="M1.2 6h9.6"/></svg>
        www.meridianrealty.net
      </span>
    </footer>
  </main>
</body>
</html>
```